HTML formatted email for Havenstrix

Create a single email in html format to describe the Havenstrix product.

It needs to be based on the brochure design (supplied) and using existing logo.
One requirement is that the background of the email has to be a set color (grey), regardless of how large the viewer opens the email window.
It will be a mix of graphics and text: and the central block of content within the email must remain intact and true regardless of how the viewer resizes the email window.
The html email must be viewable in it true format on all common email programs, including Microsoft Outlook, horde, gmail and others.

The attached file is for reference only, full PSD will be supplied to winner. (The actual text content will be different to the sample file)

```html
<!DOCTYPE html>
<html lang="en">
<head>
<meta charset="utf-8">
<title>Havenstrix – Your data when you need it</title>
<link rel="stylesheet" href="https://fonts.googleapis.com/css2?family=Arimo:wght@700&family=Yanone+Kaffeesatz:wght@400&display=swap">
<style>
  :root {
    --backdrop: #434343;
    --sheet: #ffffff;
    --ink: #111111;
    --brand-ink: #3b3b3d;
    --sky: #8fd6f4;
    --accent: #3cb4e2;
    --pin-line: #3d4a55;
  }
  html, body {
    margin: 0;
    padding: 0;
    width: 1200px;
    height: 947px;
    overflow: hidden;
    background: var(--backdrop);
  }
  .canvas {
    position: relative;
    width: 1200px;
    height: 947px;
    background: var(--backdrop);
  }
  .sheet {
    position: absolute;
    left: 0;
    top: 0;
    width: 1200px;
    height: 947px;
  }
  .brand {
    position: absolute;
    left: 192px;
    top: 300px;
    width: 300px;
    text-align: center;
  }
  .brand-dot {
    display: block;
    width: 100px;
    height: 100px;
    margin: 0 auto 18px;
    border-radius: 50%;
    background: var(--sky);
  }
  .brand-name {
    margin: 0;
    font-family: "Yanone Kaffeesatz", sans-serif;
    font-weight: 400;
    font-size: 72px;
    line-height: 1;
    color: var(--brand-ink);
  }
  .features {
    position: absolute;
    left: 548px;
    top: 307px;
    margin: 0;
    padding: 0;
    list-style: none;
  }
  .feature {
    display: flex;
    align-items: center;
    height: 59.4px;
    font-family: "Arimo", sans-serif;
    font-weight: 700;
    font-size: 18.5px;
    color: var(--ink);
  }
  .feature-pin {
    width: 18px;
    height: 20px;
    margin-right: 40px;
    flex: none;
  }
  .tagline {
    position: absolute;
    left: 580px;
    top: 847px;
    margin: 0;
    font-family: "Arimo", sans-serif;
    font-weight: 700;
    font-size: 18.5px;
    color: var(--accent);
    white-space: nowrap;
  }
</style>
</head>
<body>
<main class="canvas">
  <svg class="sheet" viewBox="0 0 849 670" width="1200" height="947" aria-hidden="true">
    <path fill="var(--sheet)" d="M766 20 H255 C150 20 92 110 89 205 C86 330 150 470 255 555 C335 618 420 640 505 640 H766 Z"/>
  </svg>

  <div class="brand">
    <span class="brand-dot"></span>
    <p class="brand-name">Havenstrix</p>
  </div>

  <ul class="features">
    <li class="feature"><svg class="feature-pin" viewBox="0 0 18 20"><path d="M9 18 C5 13 3 10.5 3 8 A6 6 0 0 1 15 8 C15 10.5 13 13 9 18 Z" fill="var(--sky)" stroke="var(--pin-line)" stroke-width="1.8"/></svg>Automadet File Backups to the cloud</li>
    <li class="feature"><svg class="feature-pin" viewBox="0 0 18 20"><path d="M9 18 C5 13 3 10.5 3 8 A6 6 0 0 1 15 8 C15 10.5 13 13 9 18 Z" fill="var(--sky)" stroke="var(--pin-line)" stroke-width="1.8"/></svg>Driftbox-style date storage service</li>
    <li class="feature"><svg class="feature-pin" viewBox="0 0 18 20"><path d="M9 18 C5 13 3 10.5 3 8 A6 6 0 0 1 15 8 C15 10.5 13 13 9 18 Z" fill="var(--sky)" stroke="var(--pin-line)" stroke-width="1.8"/></svg>Desktop file synchronisation</li>
    <li class="feature"><svg class="feature-pin" viewBox="0 0 18 20"><path d="M9 18 C5 13 3 10.5 3 8 A6 6 0 0 1 15 8 C15 10.5 13 13 9 18 Z" fill="var(--sky)" stroke="var(--pin-line)" stroke-width="1.8"/></svg>Version control of stored files</li>
    <li class="feature"><svg class="feature-pin" viewBox="0 0 18 20"><path d="M9 18 C5 13 3 10.5 3 8 A6 6 0 0 1 15 8 C15 10.5 13 13 9 18 Z" fill="var(--sky)" stroke="var(--pin-line)" stroke-width="1.8"/></svg>Cloud-based Contacts</li>
    <li class="feature"><svg class="feature-pin" viewBox="0 0 18 20"><path d="M9 18 C5 13 3 10.5 3 8 A6 6 0 0 1 15 8 C15 10.5 13 13 9 18 Z" fill="var(--sky)" stroke="var(--pin-line)" stroke-width="1.8"/></svg>Cloud-based Address Books</li>
    <li class="feature"><svg class="feature-pin" viewBox="0 0 18 20"><path d="M9 18 C5 13 3 10.5 3 8 A6 6 0 0 1 15 8 C15 10.5 13 13 9 18 Z" fill="var(--sky)" stroke="var(--pin-line)" stroke-width="1.8"/></svg>Cloud-based Calendar</li>
    <li class="feature"><svg class="feature-pin" viewBox="0 0 18 20"><path d="M9 18 C5 13 3 10.5 3 8 A6 6 0 0 1 15 8 C15 10.5 13 13 9 18 Z" fill="var(--sky)" stroke="var(--pin-line)" stroke-width="1.8"/></svg>Mobile Divice Compatible</li>
  </ul>

  <p class="tagline">Your data - when you need it where you need it</p>
</main>
</body>
</html>
```